Design für ein Flyer mit Gutschein-Abriss
Zielgruppe
Handgemachte/ handgefertigte Körperpflege- und Kosmetikprodukte, die in kleinen Chargen gefertigt werden (somit wechselnde Produkte, die in bestimmten Mengen verfügbar sind) u.a. Seifen, Rasierseifen, Badezusätze, Gesichtspflege usw.
Die Produkte werden ohne künstliche Zusätze und Konservierungsstoffe hergestellt und erhalten so wenig Allergene-Stoffe wie möglich, zum Teil vegan.
In geringem Umfang werden ebenfalls Zubehör für Körperpflege vermarktet (z.B. Lavastein für Hornhautentfernung etc.).
Die Produkte werden online und im stationären Handel vertrieben.
Ansprechen von möglichst allen Altersgruppen.
Zielgruppe: 'Otto-Normal-Verbraucher', FRAUEN, Eltern (Mutter-Kind), Männer, in geringem Umfang Haustierbesitzer (Hundeshampoos etc.)
Aufgabenstellung
Größe: DinA5
Wir führen folgende Produkte in unserer Manufaktur:
Natürliche handgefertigte Naturseifen (Milchseifen, Kräuterseifen, Aromaseifen, uvm.), Seifentorten, Seifen- und Badecupcakes, handgerollte Badetrüffel, Badesalz, Badeöle, Badeeis, Badefondant, Körper- und Gesichtspflegeprodukte, Badezubehör, Aromatherapie, Dekorationsartikel sowie Geschenkkörbe für Privat- und Firmenkunden.
Die Produkte enthalten natürliche Inhaltsstoffe, zum Teil hochwertige ätherische Öle und sind Paraben- und SLS-frei. Unsere Produkte werden nicht an Tieren getestet. Wir achten bei der Auswahl der Inhaltsstoffe und unseren Lieferanten auf fairen Handel und nachhaltige Produktion.
Des Weiteren führen wir handgemachte Sojawachskerzen, diese sind Paraffin frei und enthalten Sojawachs aus nachhaltiger Produktion.
Der Flyer soll am unteren Rand den Gutschein beinhalten, welches abgeschnitten werden kann (mit 20 % Rabatt gilt für Online und im Laden).
Auf den Flyer sollten auf jeden Fall noch folgende Daten:
Neueröffnung am 05.05.2017
www.quorvablends.de
Öffnungszeiten: Freitags von 11:00 bis 18:00 Uhr
Anbei unser Logo so wie ein Link mit Bildern einiger unserer Produkte.
https://www.filekiste-beispiel.de/s/x71tq9wpzd3k0m/BBR4uKoLmTZ8wPaYc3nH7Vxe?dl=0
Wir freuen uns schon auf viele tolle Vorschläge.

```html
<!DOCTYPE html>
<html lang="de">
<head>
<meta charset="utf-8">
<title>Quorva Blends – Flyer Neueröffnung</title>
<link rel="stylesheet" href="https://fonts.googleapis.com/css2?family=Poppins:wght@300;400;500;600&display=swap">
<style>
  :root {
    --green: #93b42b;
    --green-dark: #4f6220;
    --green-soft: #a9c64a;
    --text: #4a4a4a;
    --text-light: #6a6a6a;
    --white: #ffffff;
  }
  * { box-sizing: border-box; margin: 0; padding: 0; }
  html, body { width: 847px; height: 1200px; overflow: hidden; background: var(--white); }
  body { font-family: "Poppins", sans-serif; color: var(--text); }
  .flyer { position: relative; width: 847px; height: 1200px; background: var(--white); }

  .brand { position: absolute; right: 24px; top: 26px; width: 250px; text-align: left; }
  .brand-name { display: flex; align-items: center; gap: 12px; color: var(--green); font-size: 34px; font-weight: 500; letter-spacing: 2px; line-height: 1; }
  .brand-dot { width: 18px; height: 18px; border-radius: 50%; background: var(--green); flex: none; }
  .brand-tagline { margin-top: 14px; font-size: 11px; letter-spacing: 1.5px; color: var(--text-light); text-transform: uppercase; }

  .hero-photo { position: absolute; left: 0; top: 157px; width: 847px; height: 277px;
    background: linear-gradient(100deg, #f3e6d8 0%, #f4c6cf 22%, #fbf3ea 42%, #f1d98a 58%, #f7c9d4 78%, #f0e4e6 100%); }

  .side-panel { position: absolute; left: 0; top: 434px; width: 258px; height: 655px; background: var(--green); }
  .opening { position: absolute; left: 30px; top: 48px; color: var(--green-dark); font-size: 25px; line-height: 1.4; font-weight: 400; }

  .coupon { position: absolute; left: 0; top: 231px; width: 258px; height: 424px;
    border-top: 3px dashed var(--white); border-right: 3px dashed var(--white); }
  .coupon-deco { position: absolute; left: 40px; top: 60px; width: 180px; height: 300px; border-radius: 90px 90px 20px 20px; background: var(--green-soft); opacity: .55; }
  .coupon-text { position: absolute; left: 0; right: 0; top: 140px; text-align: center; color: var(--white); }
  .coupon-value { font-size: 76px; font-weight: 500; line-height: 1; }
  .coupon-scope { margin-top: 10px; font-size: 30px; line-height: 1.2; font-weight: 400; }

  .content { position: absolute; left: 296px; top: 462px; width: 520px; }
  .headline { font-size: 26px; font-weight: 600; color: var(--text); letter-spacing: .2px; }
  .subline { margin-top: 8px; font-size: 27px; font-weight: 400; color: var(--text-light); }
  .intro { margin-top: 20px; font-size: 20px; font-weight: 300; }
  .product-list { list-style: none; margin-top: 18px; font-size: 20px; font-weight: 300; line-height: 1.5; }
  .contact { margin-top: 30px; font-size: 20px; font-weight: 300; line-height: 1.5; }

  .badge { position: absolute; left: 585px; top: 944px; width: 262px; height: 62px; background: var(--green);
    color: var(--white); font-size: 20px; font-weight: 500; line-height: 1.3; padding: 6px 0 0 28px; }

  .footer-photo { position: absolute; left: 258px; top: 1089px; width: 589px; height: 111px;
    background: linear-gradient(90deg, #f1ebe4 0%, #c79a7a 25%, #f5efe8 50%, #b8322f 72%, #f2eeea 100%); }
</style>
</head>
<body>
<div class="flyer">
  <header class="brand">
    <div class="brand-name"><span class="brand-dot"></span>QUORVA BLENDS</div>
    <div class="brand-tagline">be natural with Quorva Blends</div>
  </header>

  <div class="hero-photo" role="img" aria-label="Foto: handgemachte Seifen-Cupcakes in Rosa, Weiß und Gelb"></div>

  <aside class="side-panel">
    <p class="opening">05.05.2017<br>Neueröffnung</p>
    <div class="coupon">
      <div class="coupon-deco" role="img" aria-label="Dezente Cupcake-Illustration im Hintergrund"></div>
      <div class="coupon-text">
        <div class="coupon-value">20%</div>
        <div class="coupon-scope">für Shop &amp;<br>onlineshop</div>
      </div>
    </div>
  </aside>

  <main class="content">
    <h1 class="headline">handgefertigt, hochwertig, limitiert.</h1>
    <p class="subline">Beauty &amp; more.</p>
    <p class="intro">Basierend auf natürlichen Inhaltsstoffen.</p>
    <ul class="product-list">
      <li>Badezubehör</li>
      <li>Aromatherapie</li>
      <li>Dekorationsartikel</li>
      <li>Geschenkkörbe</li>
    </ul>
    <p class="contact">Mühlgasse 14, 91580 Talheim<br>Öffnungszeiten: Freitags 11:00 – 18:00 Uhr<br>info@quorvablends.de, www.quorvablends.de</p>
  </main>

  <div class="badge">NO ANIMAL<br>TESTING</div>

  <div class="footer-photo" role="img" aria-label="Foto: gerollte Handtuch-Torten mit Kirschen"></div>
</div>
</body>
</html>
```